IT Company Business Card design

Brisk Node is a new computer solutions business focusing on setting up servers and computer systems for small to medium sized businesses.

A business client will either request a solution, or support for a current system and we will turn up on site to provide these services.

We are bast in Christchurch, New Zealand.

We are looking for unique business card's that stand out and show off the business in a professional light.

Open to all idea's etc.

Industry/Entity Type

Computer

Requirements
Must have
• Business Logo (AI file attached)
Employee Name
Business title
Business landline number
Cell phone number
Email
Web URL
Nice to have
• Could be nice to have some keywords (possibly on the back) such as:

Business IT solutions
Network installations
Phone solutions
Server management
Software diagnostics

The above is not needed, just an idea.

```html
<!DOCTYPE html>
<html lang="en">
<head>
<meta charset="utf-8">
<title>Brisk Node – Business Card</title>
<link rel="stylesheet" href="https://fonts.googleapis.com/css2?family=Jost:wght@300;400;700;800&display=swap">
<style>
  :root {
    --page: #ffffff;
    --card: #f8f9f9;
    --outline: #111111;
    --ink: #111111;
    --mark-blue: #1d3fae;
    --band-teal: #35ece4;
    --band-text: #ffffff;
  }
  * { margin: 0; padding: 0; box-sizing: border-box; }
  html, body {
    width: 1000px;
    height: 1200px;
    overflow: hidden;
    background: var(--page);
  }
  .sheet {
    position: relative;
    width: 1000px;
    height: 1200px;
    font-family: "Jost", "Futura", sans-serif;
    color: var(--ink);
  }
  .card-shapes {
    position: absolute;
    inset: 0;
  }
  .card-body { fill: var(--card); stroke: var(--outline); stroke-width: 3; }
  .contact-band { fill: var(--band-teal); }
  .brand-dot { fill: var(--mark-blue); }
  .text {
    position: absolute;
    line-height: 1;
    white-space: nowrap;
  }
  .brand-name {
    font-weight: 300;
    text-transform: uppercase;
  }
  .front .brand-name { left: 468px; top: 337px; font-size: 52px; letter-spacing: 3px; }
  .front .web-url { left: 502px; top: 410px; font-size: 25px; font-weight: 300; }

  .back .brand-name { left: 398px; top: 778px; font-size: 36px; letter-spacing: 2.5px; }
  .back .email { left: 622px; top: 731px; font-size: 20px; font-weight: 300; }
  .back .employee-name {
    left: 445px; top: 870px; font-size: 26px; font-weight: 800;
    transform: translateX(-50%);
  }
  .back .job-title {
    left: 445px; top: 907px; font-size: 20px; font-weight: 300;
    transform: translateX(-50%);
  }
  .back .band-label {
    top: 1000px; font-size: 20px; font-weight: 800;
    color: var(--band-text);
    transform: translateX(-50%);
  }
  .back .office { left: 285px; }
  .back .cell { left: 593px; }
</style>
</head>
<body>
<main class="sheet">
  <svg class="card-shapes" width="1000" height="1200" viewBox="0 0 1000 1200" aria-hidden="true">
    <path class="card-body" d="M95 577 L90 395 C85 250 140 165 280 160 L817 163 L815 578 Z"/>
    <circle class="brand-dot" cx="275" cy="335" r="138"/>

    <path class="card-body" d="M88 1097 L84 915 C78 770 130 685 275 680 L810 684 L808 1098 Z"/>
    <rect class="contact-band" x="89" y="990" width="719" height="106"/>
    <path d="M88 1097 L808 1098" stroke="var(--outline)" stroke-width="3" fill="none"/>
    <circle class="brand-dot" cx="308" cy="790" r="56"/>
  </svg>

  <section class="card front">
    <div class="text brand-name">Brisk Node</div>
    <div class="text web-url">Web URL</div>
  </section>

  <section class="card back">
    <div class="text email">Email</div>
    <div class="text brand-name">Brisk Node</div>
    <div class="text employee-name">Employee Name</div>
    <div class="text job-title">Title</div>
    <div class="text band-label office">Office</div>
    <div class="text band-label cell">Cell</div>
  </section>
</main>
</body>
</html>
```